The Quiet Pantry Method: Reshape Your Habits Around Meals in Only 30 Days

I want a book cover for a paperback non-fiction book 30 day challenge to transform you relationship with your food, diet and lifestyle for longterm health and vitality. I would like to incorporate two photos on the front cover, one of a Greek salad and one of me the author. I have uploaded the four photos. Use which of each pair you think best. Because of my name, I want the photo on the cover. Otherwise folks assume Marla is a guy.
I am looking at best selling health books and they seem to be on the lighter side color-wise, with horizontal design. Green and orange seem to work most often, though my logo is a bluish turquoise (https://marlavoskin.com). I would imagine a light background, clear simple fonts. Looking forward to your designs!

Target Market(s)

Women around 35-40 confused by conflicting nutrition information but dedicated to better health haelthy

Industry/Entity Type

nutrition and wellness

Font styles to use
Serif

Colors
00AB8E
00BBA5
67D7C9
C6EFE9
E9F9F6
F0912C
F2A743
F7CA91
FBE8D2
FDF5EE
EE7325
F08F49
F5BC92
FAE3D3
FDF4ED

Requirements
Must have
• Clear simple look with room for an endorsement
Nice to have
• Hints of natural scenes and happy places
Should not have
• Dark or ominous feel

```html
<!DOCTYPE html>
<html lang="en">
<head>
<meta charset="utf-8">
<title>The Quiet Pantry Method – Cover</title>
<link href="https://fonts.googleapis.com/css2?family=Playfair+Display:ital,wght@0,400;0,500;1,400&display=swap" rel="stylesheet">
<style>
  :root {
    --green-deep: #13926f;
    --green: #1fa07c;
    --orange: #e0844a;
    --orange-deep: #c96a36;
    --peach: #f0b88e;
    --cream: #fdf5ee;
    --white: #ffffff;
    --brand: #00ab8e;
    --ink-shadow: rgba(40, 50, 40, 0.5);
  }
  * { margin: 0; padding: 0; box-sizing: border-box; }
  html, body { width: 848px; height: 1200px; overflow: hidden; background: var(--cream); }
  .cover {
    position: relative;
    width: 848px;
    height: 1200px;
    overflow: hidden;
    font-family: "Playfair Display", Georgia, serif;
    font-variant-numeric: lining-nums;
    color: var(--white);
    background: linear-gradient(180deg, var(--green-deep) 0%, var(--green) 30%, #6fa36e 46%, var(--orange) 58%, var(--orange-deep) 100%);
  }
  .portrait-backdrop {
    position: absolute;
    top: 0; right: 0;
    width: 440px; height: 420px;
    background:
      radial-gradient(ellipse 190px 210px at 62% 42%, rgba(170, 215, 190, 0.55) 0%, rgba(120, 195, 165, 0.35) 55%, rgba(31, 160, 124, 0) 100%),
      linear-gradient(200deg, rgba(60, 140, 110, 0.35), rgba(31, 160, 124, 0) 70%);
  }
  .field-scene {
    position: absolute;
    left: 0; top: 560px;
    width: 848px; height: 420px;
    background:
      radial-gradient(circle at 370px 217px, rgba(255, 240, 215, 1) 0, rgba(252, 220, 180, 0.95) 62px, rgba(240, 170, 110, 0.5) 110px, rgba(220, 130, 75, 0) 210px),
      linear-gradient(180deg, rgba(200, 110, 60, 0) 0%, rgba(180, 95, 50, 0.45) 45%, rgba(165, 85, 45, 0.6) 100%);
  }
  .produce-table {
    position: absolute;
    left: 0; top: 850px;
    width: 848px; height: 350px;
    background:
      radial-gradient(ellipse 150px 120px at 120px 180px, rgba(250, 225, 200, 0.9), rgba(250, 225, 200, 0) 100%),
      radial-gradient(ellipse 120px 90px at 260px 270px, rgba(245, 170, 120, 0.85), rgba(245, 170, 120, 0) 100%),
      radial-gradient(ellipse 90px 130px at 560px 110px, rgba(150, 80, 45, 0.7), rgba(150, 80, 45, 0) 100%),
      radial-gradient(ellipse 120px 110px at 650px 220px, rgba(245, 210, 175, 0.85), rgba(245, 210, 175, 0) 100%),
      radial-gradient(ellipse 110px 160px at 790px 190px, rgba(200, 130, 90, 0.8), rgba(200, 130, 90, 0) 100%),
      linear-gradient(180deg, rgba(200, 120, 75, 0.2) 0%, rgba(225, 150, 105, 0.75) 45%, rgba(200, 120, 80, 0.9) 100%);
  }
  .title {
    position: absolute;
    left: 60px; top: 72px;
    font-size: 92px;
    font-weight: 400;
    line-height: 130px;
    letter-spacing: -1px;
    text-shadow: 3px 5px 7px var(--ink-shadow);
  }
  .subtitle {
    position: absolute;
    left: 86px; top: 378px;
    padding-left: 36px;
    border-left: 6px solid rgba(255, 255, 255, 0.75);
    font-size: 52px;
    line-height: 72px;
    text-shadow: 2px 3px 5px var(--ink-shadow);
  }
  .badge {
    position: absolute;
    left: 610px; top: 382px;
    width: 215px; height: 215px;
  }
  .badge-text {
    position: absolute;
    left: 610px; top: 420px;
    width: 215px;
    text-align: center;
    line-height: 1;
    text-shadow: 2px 3px 4px rgba(120, 60, 20, 0.5);
  }
  .badge-number { display: block; font-size: 100px; }
  .badge-unit { display: block; font-size: 36px; margin-top: 0; }
  .author-photo {
    position: absolute;
    left: 325px; top: 893px;
    width: 200px; height: 200px;
    border-radius: 10px;
    background: linear-gradient(180deg, #8e9ea6 0%, #a9aeb0 50%, #e8dcc6 100%);
    box-shadow: 0 3px 8px rgba(0, 0, 0, 0.25);
  }
  .author-name {
    position: absolute;
    left: 0; width: 848px; top: 1100px;
    text-align: center;
    font-style: italic;
    font-size: 21px;
    line-height: 1.25;
    text-shadow: 1px 1px 3px var(--ink-shadow);
  }
  .author-name .site { display: block; font-size: 19px; }
  .brand-mark {
    position: absolute;
    left: 745px; top: 1111px;
    width: 66px; height: 66px;
    border-radius: 50%;
    background: var(--white);
    color: var(--brand);
    font-size: 14px;
    display: flex; align-items: center; justify-content: center;
  }
</style>
</head>
<body>
<main class="cover">
  <div class="portrait-backdrop" role="img" aria-label="Photo of a smiling woman with long hair, softly faded into the green background"></div>
  <div class="field-scene" role="img" aria-label="Photo of wheat stalks against a glowing sunset"></div>
  <div class="produce-table" role="img" aria-label="Photo of fresh Greek salad ingredients: celery, carrots, peppers, onion, olive oil bottles and jars on a counter"></div>

  <h1 class="title">The Quiet Pantry<br>Method</h1>
  <p class="subtitle">Reshape Your<br>Habits Around<br>Meals in Only 30<br>Days</p>

  <svg class="badge" viewBox="0 0 220 220" aria-hidden="true">
    <defs>
      <linearGradient id="badgeFill" x1="0" y1="0" x2="0" y2="1">
        <stop offset="0" stop-color="#f7b24a"/>
        <stop offset="1" stop-color="#ee8a2c"/>
      </linearGradient>
    </defs>
    <polygon fill="url(#badgeFill)" points="110,5 132,30 165,20 170,53 203,63 188,92 212,115 185,135 198,166 164,170 158,203 127,190 110,215 93,190 62,203 56,170 22,166 35,135 8,115 32,92 17,63 50,53 55,20 88,30"/>
  </svg>
  <div class="badge-text">
    <span class="badge-number">30</span>
    <span class="badge-unit">days</span>
  </div>

  <div class="author-photo" role="img" aria-label="Portrait photo of the author, Marla Voskin"></div>
  <p class="author-name">Marla Voskin<span class="site">www.marlavoskin.com</span></p>

  <div class="brand-mark">Voskin</div>
</main>
</body>
</html>
```